Roadwise Beacon Traffic Control Company Website

Modern website Wordpress design using all greyscale photos with a pop of red (such as road closure signs or detour cones) for strategic emphasis. (see brand guide for color codes)
The creative goal is to leverage high-contrast, desaturated imagery to create a clean, professional, and industrial feel. The selective use of red will draw immediate attention to critical elements—such as road hazards, safety equipment, or key messages to ensure the viewer's focus is directed with purpose.

Brand guide, homepage content and logo are attached. Create clean professional user experience to market services to industry professionals.

```html
<!DOCTYPE html>
<html lang="en">
<head>
<meta charset="utf-8">
<title>Roadwise Beacon — Traffic Control Solutions</title>
<link href="https://fonts.googleapis.com/css2?family=Inter+Tight:wght@400;500&display=swap" rel="stylesheet">
<style>
  :root {
    --cream: #f5f0ea;
    --red: #e81e25;
    --black: #000000;
    --white: #ffffff;
    --ink: #1a1a1a;
    --muted: #555555;
    --rule: #3a3a3a;
    --amber: #f2c230;
  }
  * { margin: 0; padding: 0; box-sizing: border-box; }
  html, body { width: 672px; height: 1200px; overflow: hidden; }
  body {
    position: relative;
    background: var(--cream);
    font-family: "Inter Tight", Arial, sans-serif;
    color: var(--ink);
  }
  .abs { position: absolute; }

  /* Hero */
  .hero {
    left: 11px; top: 11px; width: 650px; height: 289px;
    background:
      radial-gradient(circle at 72% 48%, #8a1414 0%, #4a0a0a 28%, rgba(20,10,10,0.95) 48%, rgba(20,20,20,0) 62%),
      linear-gradient(90deg, #5b6a72 0%, #3b474d 35%, #1a1a1a 70%, #0d0d0d 100%);
  }
  .menu-btn {
    left: 39px; top: 41px; width: 22px; height: 22px;
    background: var(--white);
    display: flex; align-items: center; justify-content: center;
  }
  .menu-btn span { display: block; width: 10px; height: 0.6px; background: #888; box-shadow: 0 2px 0 #888; margin-top: -2px; }
  .menu-label { left: 70px; top: 48px; font-size: 6.5px; color: var(--white); letter-spacing: 0.2px; }
  .brand {
    left: 296px; top: 40px; width: 80px; height: 26px;
    display: flex; align-items: center; justify-content: center; gap: 4px;
    color: var(--white); font-size: 9px; font-weight: 500; letter-spacing: 0.3px; text-transform: uppercase;
  }
  .brand i { display: block; width: 6px; height: 6px; background: var(--red); }
  .cta {
    left: 566px; top: 41px; width: 67px; height: 22px;
    background: var(--white); color: var(--black);
    font-size: 6.5px; display: flex; align-items: center; justify-content: center;
  }
  .hero-title {
    left: 11px; top: 118px; width: 650px;
    text-align: center; color: var(--white);
    font-size: 34px; line-height: 36px; font-weight: 400; letter-spacing: -0.6px;
  }

  /* Services */
  .eyebrow { left: 39px; top: 336px; font-size: 7px; letter-spacing: 0.2px; }
  .section-title {
    left: 39px; top: 360px; font-size: 33.5px; line-height: 37px;
    font-weight: 400; letter-spacing: -0.6px; color: var(--black);
  }
  .card { top: 473px; width: 246px; height: 182px; padding: 28px; }
  .card--red { background: var(--red); color: var(--white); }
  .card--white { background: var(--white); color: var(--muted); }
  .card-num { font-size: 5px; margin-top: 2px; }
  .card-title { font-size: 14px; line-height: 15px; margin-top: 16px; letter-spacing: -0.1px; }
  .card-icon { position: absolute; right: 20px; bottom: 22px; }
  .card-3 { left: 575px; width: 97px; overflow: hidden; white-space: nowrap; }
  .slider-nav {
    left: 596px; top: 606px; width: 56px; height: 56px; border-radius: 50%;
    background: var(--black); display: flex; align-items: center; justify-content: center;
  }

  /* Industries */
  .dark-band { left: 0; top: 947px; width: 672px; height: 253px; background: var(--black); }
  .industry-photo {
    left: 39px; top: 692px; width: 594px; height: 284px;
    background:
      linear-gradient(180deg, rgba(0,0,0,0) 40%, rgba(0,0,0,0.55) 100%),
      radial-gradient(circle at 26% 35%, #c33a2c 0%, rgba(195,58,44,0) 14%),
      radial-gradient(circle at 55% 55%, #b5382a 0%, rgba(181,56,42,0) 10%),
      linear-gradient(100deg, #6b2a2a 0%, #8c8682 35%, #9a9590 60%, #6e7688 100%);
  }
  .industry-title {
    left: 68px; top: 838px; color: var(--white);
    font-size: 34px; line-height: 36px; font-weight: 400; letter-spacing: -0.6px;
  }
  .sector { display: flex; align-items: center; gap: 8px; color: var(--white); font-size: 12px; }
  .sector svg { flex: none; }
  .rule { left: 39px; width: 594px; height: 1px; background: var(--rule); }
  .promise { display: flex; align-items: center; gap: 3px; color: var(--white); font-size: 14px; font-weight: 500; }
  .to-top {
    left: 605px; top: 1098px; width: 28px; height: 28px; border-radius: 50%;
    background: var(--white); display: flex; align-items: center; justify-content: center;
  }

  /* Footer */
  .footer-copy { left: 39px; top: 1166px; font-size: 6.5px; color: var(--white); }
  .footer-nav { left: 252px; top: 1166px; font-size: 6.5px; color: var(--white); display: flex; gap: 3px; }
  .badge { left: 575px; top: 1161px; width: 58px; height: 18px; background: #d9d9d9; border-radius: 2px; }
</style>
</head>
<body>

  <!-- Hero -->
  <div class="abs hero" role="img" aria-label="Greyscale city street in the rain with a glowing red traffic light in close-up"></div>
  <div class="abs menu-btn"><span></span></div>
  <div class="abs menu-label">MENU</div>
  <div class="abs brand"><i></i>Roadwise Beacon</div>
  <a class="abs cta">Get in Touch</a>
  <h1 class="abs hero-title">Traffic Control Solutions<br>Engineered For Safety.</h1>

  <!-- Services -->
  <div class="abs eyebrow">SERVICES</div>
  <h2 class="abs section-title">Safety isn’t a priority,<br>it’s the foundation of everything we do</h2>

  <div class="abs card card--red" style="left:39px">
    <div class="card-num">01</div>
    <div class="card-title">Flagging &amp; Lane Closures</div>
    <svg class="card-icon" width="36" height="32" viewBox="0 0 36 32" fill="none" stroke="#fff" stroke-width="1.6">
      <path d="M2 31 L4 14 H9 L8 31 Z"/>
      <path d="M34 31 L32 14 H27 L28 31 Z"/>
      <path d="M2 31 H34"/>
      <path d="M18 16 V1 H25 L22 4 L25 7 H18"/>
      <path d="M18 24 V28"/>
    </svg>
  </div>

  <div class="abs card card--white" style="left:307px">
    <div class="card-num">02</div>
    <div class="card-title">Temporary Traffic Control Plans<br>(TTCPs)</div>
    <svg class="card-icon" width="22" height="32" viewBox="0 0 22 32" fill="none" stroke="#555" stroke-width="1.8">
      <rect x="4" y="1" width="14" height="30" rx="2"/>
      <circle cx="11" cy="8" r="2.5" fill="#555"/>
      <circle cx="11" cy="16" r="2.5" fill="#555"/>
      <circle cx="11" cy="24" r="2.5" fill="#555"/>
      <path d="M1 8 H4 M1 16 H4 M1 24 H4 M18 8 H21 M18 16 H21 M18 24 H21"/>
    </svg>
  </div>

  <div class="abs card card--red card-3">
    <div class="card-num">03</div>
    <div class="card-title">Signage &amp; Devices</div>
  </div>

  <div class="abs slider-nav">
    <svg width="22" height="14" viewBox="0 0 22 14" fill="none" stroke="#fff" stroke-width="1.4">
      <path d="M7 1 L1 7 L7 13"/><path d="M15 1 L21 7 L15 13"/>
    </svg>
  </div>

  <!-- Industries -->
  <div class="abs dark-band"></div>
  <div class="abs industry-photo" role="img" aria-label="Greyscale crosswalk with red traffic cones as a traffic supervisor talks with a driver"></div>
  <h2 class="abs industry-title">Serving Texas Industry to<br>Ensure Safety, Compliance,<br>and Efficient Traffic Flow</h2>

  <div class="abs sector" style="left:68px; top:995px">
    <svg width="18" height="16" viewBox="0 0 18 16" fill="none" stroke="#fff" stroke-width="1">
      <path d="M4 1 L1 15 M14 1 L17 15 M9 2 V4 M9 7 L6 15 M9 7 L12 15 M7 12 H11"/>
    </svg>
    Road construction, maintenance, &amp; Detours
  </div>
  <div class="abs sector" style="left:348px; top:995px">
    <svg width="21" height="10" viewBox="0 0 21 10" fill="none" stroke="#fff" stroke-width="1.2">
      <rect x="0.6" y="0.6" width="19.8" height="8.8" rx="4.4"/>
      <circle cx="5.5" cy="5" r="2.4" fill="#fff"/><circle cx="10.5" cy="5" r="2.4" fill="#fff"/><circle cx="15.5" cy="5" r="2.4" fill="#fff"/>
    </svg>
    Municipal &amp; State projects
  </div>
  <div class="abs sector" style="left:68px; top:1028px">
    <svg width="20" height="18" viewBox="0 0 20 18" fill="none" stroke="#fff" stroke-width="1">
      <rect x="1" y="7" width="11" height="8"/><path d="M3 10 H10 M3 12 H10 M1 17 H13 M12 11 L19 3 M15 1 L19 3 L17 6"/>
    </svg>
    Private Sector &amp; Commercial Contractors
  </div>
  <div class="abs sector" style="left:348px; top:1028px">
    <svg width="20" height="18" viewBox="0 0 20 18" fill="none" stroke="#fff" stroke-width="1">
      <circle cx="10" cy="4" r="2.5"/><path d="M10 0 V1 M6 4 H7 M13 4 H14 M3 17 L6 8 H14 L17 17 Z M4.5 12.5 H15.5 M10 8 V17"/>
    </svg>
    Oil, Gas, Wind, Solar, &amp; Manufacturing
  </div>

  <div class="abs rule" style="top:1063px"></div>

  <div class="abs promise" style="left:68px; top:1081px">
    <svg width="14" height="12" viewBox="0 0 14 12"><rect x="0" y="2" width="14" height="5" fill="#f2c230"/><path d="M2 2 L0 7 M6 2 L4 7 M10 2 L8 7 M14 2 L12 7" stroke="#222" stroke-width="1.4"/><path d="M2 0 V12 M12 0 V12" stroke="#f2c230" stroke-width="1.4"/></svg>
    StateRoad-Compliant &amp; Certified
  </div>
  <div class="abs promise" style="left:348px; top:1081px">
    <svg width="14" height="12" viewBox="0 0 14 12"><rect x="0" y="2" width="14" height="5" fill="#f2c230"/><path d="M2 2 L0 7 M6 2 L4 7 M10 2 L8 7 M14 2 L12 7" stroke="#222" stroke-width="1.4"/><path d="M2 0 V12 M12 0 V12" stroke="#f2c230" stroke-width="1.4"/></svg>
    Experienced &amp; Trained Crew
  </div>
  <div class="abs promise" style="left:68px; top:1106px">
    <svg width="14" height="12" viewBox="0 0 14 12"><rect x="0" y="2" width="14" height="5" fill="#f2c230"/><path d="M2 2 L0 7 M6 2 L4 7 M10 2 L8 7 M14 2 L12 7" stroke="#222" stroke-width="1.4"/><path d="M2 0 V12 M12 0 V12" stroke="#f2c230" stroke-width="1.4"/></svg>
    Reliable &amp; Responsive
  </div>
  <div class="abs promise" style="left:349px; top:1106px">
    <svg width="14" height="12" viewBox="0 0 14 12"><rect x="0" y="2" width="14" height="5" fill="#f2c230"/><path d="M2 2 L0 7 M6 2 L4 7 M10 2 L8 7 M14 2 L12 7" stroke="#222" stroke-width="1.4"/><path d="M2 0 V12 M12 0 V12" stroke="#f2c230" stroke-width="1.4"/></svg>
    Cost-Effective &amp; Efficient
  </div>

  <div class="abs to-top">
    <svg width="12" height="8" viewBox="0 0 12 8" fill="none" stroke="#000" stroke-width="1.8"><path d="M1 7 L6 2 L11 7"/></svg>
  </div>

  <div class="abs rule" style="top:1141px"></div>

  <!-- Footer -->
  <div class="abs footer-copy">© 2025 Roadwise Beacon. All right reserved.</div>
  <nav class="abs footer-nav">
    <span>Home</span><span>.</span><span>About</span><span>.</span><span>Services</span><span>.</span><span>Rentals</span><span>.</span><span>Jobs</span><span>.</span><span>Contact</span>
  </nav>
  <div class="abs badge" aria-label="Industry association membership badge"></div>

</body>
</html>
```